Business Cards Needed For Veterinary Business

Looking for a business card design for a veterinary blood bank. We would like it to be clean and professional on appearance but still warm and inviting. We would like to utilize our logo and similar coloring. We will use our phone number, email, website, employee name, employee title.

We do not want a bunch of animated animal photos but do not need the style to be as clinical as a laboratory or human medical procedure office.

We are looking for some creative ideas to choose from so that we can generate a standout professional business card for our management team to utilize.

Target Market(s)

professionals

Industry/Entity Type

veterinary

Contact Information for Business Card

employee name, employee title, phone number, website URL, email

Font styles to use
Sans Serif

Colors
0054AA
0677BA
7BADD7
CADEEF
E8F1F8
EB3D1F
EC4F4E
F09395
F8D3D4
FCEDEE

Requirements
Nice to have
• creative design
Should not have
• animated photos

```html
<!DOCTYPE html>
<html lang="en">
<head>
<meta charset="utf-8">
<title>Harbor Veterinary Blood Bank – Business Cards</title>
<link href="https://fonts.googleapis.com/css2?family=Montserrat:wght@700&family=Roboto:wght@400&display=swap" rel="stylesheet">
<style>
  :root {
    --brand-red: #EA1D2C;
    --accent-red: #EC4F4E;
    --soft-red: #F8D3D4;
    --pale-red: #FCEDEE;
    --brand-blue: #0054AA;
    --mid-blue: #0677BA;
    --paper: #FFFFFF;
    --backdrop: #EEF1F4;
  }
  * { box-sizing: border-box; margin: 0; padding: 0; }
  html, body {
    width: 1200px; height: 886px; overflow: hidden;
    background: var(--backdrop);
  }
  .sheet {
    width: 1200px; height: 886px;
    display: flex; align-items: center; justify-content: center; gap: 40px;
  }
  .card {
    width: 540px; height: 309px; position: relative; overflow: hidden;
    box-shadow: 0 10px 28px rgba(0,0,0,0.18);
  }
  /* Front */
  .card--front {
    background: var(--brand-red);
    display: flex; align-items: center; justify-content: center;
  }
  .wordmark {
    display: flex; align-items: center; gap: 16px;
    color: var(--paper);
    font-family: "Montserrat", sans-serif; font-weight: 700;
  }
  .wordmark__dot {
    width: 54px; height: 54px; border-radius: 50%; background: var(--paper);
  }
  .wordmark__text { line-height: 1.05; }
  .wordmark__main { font-size: 46px; letter-spacing: 1px; }
  .wordmark__sub { font-size: 13.5px; letter-spacing: 1.2px; }

  /* Back */
  .card--back { background: var(--paper); }
  .back__mark {
    position: absolute; left: 30px; top: 42px;
    display: flex; align-items: center; gap: 10px;
    color: var(--brand-red);
    font-family: "Montserrat", sans-serif; font-weight: 700;
  }
  .back__mark .wordmark__dot { width: 30px; height: 30px; background: var(--brand-red); }
  .back__mark .wordmark__main { font-size: 24px; letter-spacing: 0.5px; }
  .back__mark .wordmark__sub { font-size: 7.5px; letter-spacing: 0.8px; }

  .back__feature {
    position: absolute; right: 0; top: 0; width: 200px; height: 309px;
    background: linear-gradient(160deg, var(--soft-red), var(--pale-red));
  }
  .person { position: absolute; left: 30px; top: 134px; }
  .person__name {
    font-family: "Montserrat", sans-serif; font-weight: 700;
    font-size: 26px; color: var(--brand-red);
  }
  .person__title {
    font-family: "Roboto", sans-serif; font-size: 17px; color: var(--mid-blue);
    margin-top: 2px;
  }
  .contact {
    position: absolute; left: 30px; top: 210px; list-style: none;
    font-family: "Roboto", sans-serif; font-size: 15.5px; color: var(--brand-blue);
  }
  .contact__item { display: flex; align-items: center; gap: 12px; height: 28px; }
  .contact__icon {
    width: 20px; height: 20px; border-radius: 5px; background: var(--brand-red);
    display: flex; align-items: center; justify-content: center;
  }
  .contact__icon svg { width: 12px; height: 12px; }
</style>
</head>
<body>
<main class="sheet">
  <section class="card card--front" aria-label="Card front">
    <div class="wordmark">
      <span class="wordmark__dot"></span>
      <div class="wordmark__text">
        <div class="wordmark__main">HARBOR</div>
        <div class="wordmark__sub">VETERINARY BLOOD BANK</div>
      </div>
    </div>
  </section>

  <section class="card card--back" aria-label="Card back">
    <div class="back__feature" role="img" aria-label="Large brand emblem decoration area"></div>

    <div class="back__mark">
      <span class="wordmark__dot"></span>
      <div class="wordmark__text">
        <div class="wordmark__main">HARBOR</div>
        <div class="wordmark__sub">VETERINARY BLOOD BANK</div>
      </div>
    </div>

    <div class="person">
      <div class="person__name">Dana M. Whitlock</div>
      <div class="person__title">Founder and CEO</div>
    </div>

    <ul class="contact">
      <li class="contact__item">
        <span class="contact__icon">
          <svg viewBox="0 0 24 24" fill="#fff"><path d="M6.6 10.8a15 15 0 0 0 6.6 6.6l2.2-2.2a1 1 0 0 1 1-.25 11.4 11.4 0 0 0 3.6.57 1 1 0 0 1 1 1V20a1 1 0 0 1-1 1A17 17 0 0 1 3 4a1 1 0 0 1 1-1h3.5a1 1 0 0 1 1 1c0 1.25.2 2.45.57 3.57a1 1 0 0 1-.25 1z"/></svg>
        </span>
        (555) 014-2736
      </li>
      <li class="contact__item">
        <span class="contact__icon">
          <svg viewBox="0 0 24 24" fill="none" stroke="#fff" stroke-width="2.4"><rect x="3" y="5" width="18" height="14" rx="1"/><path d="M3 6l9 7 9-7"/></svg>
        </span>
        DanaMWhitlock@mail.com
      </li>
      <li class="contact__item">
        <span class="contact__icon">
          <svg viewBox="0 0 24 24" fill="none" stroke="#fff" stroke-width="2"><circle cx="12" cy="12" r="9"/><path d="M3 12h18M12 3c3 3 3 15 0 18M12 3c-3 3-3 15 0 18"/></svg>
        </span>
        www.harborvetblood.com
      </li>
    </ul>
  </section>
</main>
</body>
</html>
```